Visitenkarten
Zielgruppe
Hallo!
Für mein Unternehmen habe ich bereits einmal ein Logo mit Feldmotte erstellen lassen (leider weiß ich den Designer nicht mehr).
Unter meinem Unternehmen Vollmerhaus Coaching laufen zwei Unternehmensbereiche, für die ich jetzt Visitenkarten benötige. Daher ist der Stil der beiden Teilbereiche ähnlich. Die Logos existieren schon. Nun benötige ich für beide Bereiche Visitenkarten. Für beide Bereiche benötige ich im Anschluss im 1:1 Auftrage noch Dateien, damit die ich Logos auch gut auf Webseiten und Social Medien nutzen kann.
Vollmerhaus HR Services <: bietet HR Dienstleistungen rund um das Personalwesen an: HR-Trainings, HR Outsourcing und Projekt- und Interimsmanagement
Sattelklar Balance | Vollmerhaus Coaching: bietet Mental- und Hypnosecoachings an, Trainings zur mentalen Fitness, Stress- und Blockadenlösung im Reitsport und optimale Turniervorbereitung
Aufgabenstellung
Bitte den bestehenden Brandguide und die Materialien nutzen. Eigene Ideen sind willkommen, sollen aber in der Logik bleiben.
Daten Visitenkarte Vollmerhaus HR Services:
Annelie Vollmerhaus
Dipl. Sozialwirt, Business Coach, Mentaltrainer
Telefon +49 (0)1593 26 48 357
Mobil +49 (0)171 58 93 704
Mail: annelie@vollmerhaus-beratung.example
Vollmerhaus HR Services | Vollmerhaus Coaching
Am Lindenhang 9b
31547 Lindwerder
Daten Visitenkarte Vollmerhaus Sattelklar Balance:
Dipl. Sozialwirt, Hypnosecoach, Mentaltrainer
Sattelklar Balance | Vollmerhaus Coaching

```html
<!DOCTYPE html>
<html lang="de">
<head>
<meta charset="utf-8">
<title>Visitenkarten – Vollmerhaus Coaching</title>
<link href="https://fonts.googleapis.com/css2?family=Archivo:wght@400;700&family=Arimo:wght@400&display=swap" rel="stylesheet">
<style>
  :root{
    --backdrop:#6b5a8e;
    --card:#ffffff;
    --purple:#4f4283;
    --purple-light:#6e5fa3;
    --purple-dark:#2f2650;
    --ink:#2b2248;
    --text:#2e2a3a;
    --sketch:#b7addb;
  }
  *{box-sizing:border-box;margin:0;padding:0}
  html,body{width:960px;height:1200px;overflow:hidden}
  body{background:var(--backdrop);font-family:"Arimo",Arial,sans-serif;color:var(--text);
    display:flex;align-items:center;justify-content:center}
  .sheet{display:grid;grid-template-columns:430px 430px;gap:36px 30px}
  .card{position:relative;width:430px;height:278px;background:var(--card);overflow:hidden;
    box-shadow:0 10px 24px rgba(30,20,60,.35)}
  .card__corners{position:absolute;inset:0;width:100%;height:100%}
  .brand{position:absolute;font-family:"Archivo",sans-serif;font-weight:400;color:var(--ink);
    letter-spacing:.06em;text-transform:uppercase;text-align:center;line-height:1.2}
  .brand--front{left:0;right:0;top:118px;font-size:26px}
  .brand--side{left:18px;width:156px;top:150px;font-size:15px}
  .brand--riding-front{left:240px;width:160px;top:108px;font-size:15px}
  .brand--riding-side{left:106px;width:74px;top:92px;font-size:9.5px;text-align:left}
  .brand small{display:block;font-size:.55em;letter-spacing:.16em;margin-top:3px}
  .brand--riding-side small{letter-spacing:.08em}
  .sketch{position:absolute;border-radius:6px;background:linear-gradient(160deg,#e9e5f6,var(--sketch))}
  .sketch--front{left:120px;top:72px;width:110px;height:128px}
  .sketch--side{left:28px;top:58px;width:72px;height:80px}
  .band{position:absolute;top:0;bottom:0;left:186px;width:30px;
    background:linear-gradient(180deg,var(--purple-light),var(--purple-dark))}
  .band__icons{position:absolute;left:0;width:30px;top:134px;display:flex;flex-direction:column;align-items:center;gap:12px}
  .band__icons svg{width:14px;height:14px}
  .contact{position:absolute;left:232px;top:40px;right:14px}
  .contact__name{font-family:"Archivo",sans-serif;font-weight:700;font-size:19px;letter-spacing:.06em;
    line-height:1.08;color:var(--ink);text-transform:uppercase}
  .contact__role{margin-top:6px;font-size:8.4px;letter-spacing:.08em;text-transform:uppercase;line-height:1.25}
  .contact__list{list-style:none;margin-top:12px;font-size:9.4px;letter-spacing:.04em;line-height:1.25}
  .contact__list li{height:18px;white-space:nowrap}
  .contact__list li.address{height:auto;margin-top:2px}
</style>
</head>
<body>
<main class="sheet">

  <section class="card card--front">
    <svg class="card__corners" viewBox="0 0 430 278" preserveAspectRatio="none" aria-hidden="true">
      <polygon points="0,0 62,0 0,42" fill="var(--purple)"/>
      <polygon points="70,0 86,0 0,58 0,48" fill="var(--purple)"/>
      <rect x="330" y="0" width="100" height="14" fill="var(--purple)"/>
      <rect x="0" y="262" width="150" height="16" fill="var(--purple)"/>
      <polygon points="430,196 430,278 350,278" fill="var(--purple)"/>
      <polygon points="430,226 430,240 374,278 360,278" fill="#fff"/>
    </svg>
    <div class="sketch sketch--front" role="img" aria-label="Zeichnung eines galoppierenden Pferdes"></div>
    <div class="brand brand--riding-front">Sattelklar Balance<small>by Vollmerhaus Coaching</small></div>
  </section>

  <section class="card card--contact">
    <svg class="card__corners" viewBox="0 0 430 278" preserveAspectRatio="none" aria-hidden="true">
      <polygon points="0,0 62,0 0,42" fill="var(--purple)"/>
      <polygon points="70,0 86,0 0,58 0,48" fill="var(--purple)"/>
      <polygon points="430,196 430,278 350,278" fill="var(--purple)"/>
      <polygon points="430,226 430,240 374,278 360,278" fill="#fff"/>
    </svg>
    <div class="sketch sketch--side" role="img" aria-label="Zeichnung eines galoppierenden Pferdes"></div>
    <div class="brand brand--riding-side">Sattelklar Balance<small>by Vollmerhaus Coaching</small></div>
    <div class="band">
      <div class="band__icons" aria-hidden="true">
        <svg viewBox="0 0 16 16"><path d="M4 1l3 3-2 2c1 2 3 4 5 5l2-2 3 3-2 3C7 15 1 9 1 3z" fill="#fff"/></svg>
        <svg viewBox="0 0 16 16"><rect x="4" y="1" width="8" height="14" rx="1.5" fill="none" stroke="#fff" stroke-width="1.6"/><circle cx="8" cy="12.5" r="1" fill="#fff"/></svg>
        <svg viewBox="0 0 16 16"><rect x="1" y="3" width="14" height="10" fill="#fff"/><path d="M1 3l7 6 7-6" fill="none" stroke="var(--purple)" stroke-width="1.3"/></svg>
        <svg viewBox="0 0 16 16"><path d="M8 1a5 5 0 0 1 5 5c0 4-5 9-5 9S3 10 3 6a5 5 0 0 1 5-5z" fill="#fff"/><circle cx="8" cy="6" r="2" fill="var(--purple)"/></svg>
      </div>
    </div>
    <div class="contact">
      <h2 class="contact__name">Annelie<br>Vollmerhaus</h2>
      <p class="contact__role">Dipl. Sozialwirt, Hypnosecoach,<br>Mentaltrainer</p>
      <ul class="contact__list">
        <li>+49 (0)1593 26 48 357</li>
        <li>+49 (0)171 58 93 704</li>
        <li>annelie@vollmerhaus-beratung.example</li>
        <li class="address">Sattelklar Balance |<br>Vollmerhaus Coaching<br>Am Lindenhang 9b<br>31547 Lindwerder</li>
      </ul>
    </div>
  </section>

  <section class="card card--front">
    <svg class="card__corners" viewBox="0 0 430 278" preserveAspectRatio="none" aria-hidden="true">
      <polygon points="0,0 62,0 0,42" fill="var(--purple)"/>
      <polygon points="70,0 86,0 0,58 0,48" fill="var(--purple)"/>
      <rect x="330" y="0" width="100" height="14" fill="var(--purple)"/>
      <rect x="0" y="262" width="150" height="16" fill="var(--purple)"/>
      <polygon points="430,196 430,278 350,278" fill="var(--purple)"/>
      <polygon points="430,226 430,240 374,278 360,278" fill="#fff"/>
    </svg>
    <div class="brand brand--front">Vollmerhaus<small>Coaching</small></div>
  </section>

  <section class="card card--contact">
    <svg class="card__corners" viewBox="0 0 430 278" preserveAspectRatio="none" aria-hidden="true">
      <polygon points="0,0 62,0 0,42" fill="var(--purple)"/>
      <polygon points="70,0 86,0 0,58 0,48" fill="var(--purple)"/>
      <polygon points="430,196 430,278 350,278" fill="var(--purple)"/>
      <polygon points="430,226 430,240 374,278 360,278" fill="#fff"/>
    </svg>
    <div class="brand brand--side">Vollmerhaus<small>Coaching</small></div>
    <div class="band">
      <div class="band__icons" aria-hidden="true">
        <svg viewBox="0 0 16 16"><path d="M4 1l3 3-2 2c1 2 3 4 5 5l2-2 3 3-2 3C7 15 1 9 1 3z" fill="#fff"/></svg>
        <svg viewBox="0 0 16 16"><rect x="4" y="1" width="8" height="14" rx="1.5" fill="none" stroke="#fff" stroke-width="1.6"/><circle cx="8" cy="12.5" r="1" fill="#fff"/></svg>
        <svg viewBox="0 0 16 16"><rect x="1" y="3" width="14" height="10" fill="#fff"/><path d="M1 3l7 6 7-6" fill="none" stroke="var(--purple)" stroke-width="1.3"/></svg>
        <svg viewBox="0 0 16 16"><path d="M8 1a5 5 0 0 1 5 5c0 4-5 9-5 9S3 10 3 6a5 5 0 0 1 5-5z" fill="#fff"/><circle cx="8" cy="6" r="2" fill="var(--purple)"/></svg>
      </div>
    </div>
    <div class="contact">
      <h2 class="contact__name">Annelie<br>Vollmerhaus</h2>
      <p class="contact__role">Dipl. Sozialwirt,<br>Business Coach, Mentaltrainer</p>
      <ul class="contact__list">
        <li>+49 (0)1593 26 48 357</li>
        <li>+49 (0)171 58 93 704</li>
        <li>annelie@vollmerhaus-beratung.example</li>
        <li class="address">Vollmerhaus HR Services |<br>Vollmerhaus Coaching<br>Am Lindenhang 9b<br>31547 Lindwerder</li>
      </ul>
    </div>
  </section>

</main>
</body>
</html>
```